A new medical waste company needs an attractive and modern flyer.

We are a new medical waste company disposing of biohazards waste, red bag waste and sharps disposal with a focus on customer service.

Background Information

Company Name
Korvane Waste

Industry
Medical waste management

Description of the organization and its target audience

We are a new medical waste company disposing of biohazardous waste, red bag waste and medical sharps.

Description

MODERN & ELEGANT HALF PAGE FLYER

Half page mailer (front and back) with a large image related to the medical field.

The Korvane Waste logo, with the company tag line “compliant waste solutions” should also be on front of the mailer.

Website (korvanewaste.example) & email (info@korvanewsate.example) on both sides of the flyer

Main headline
-Now you have options for your medical waste disposal

Who we serve
- Dentist
- Physicians
-Blood banks
-Tattoo parlors
-Assisted living facilities
-Laboratories
-Veterinarians

What we offer
-Straight forward pricing
-No hidden fees
-No long term contracts
-Free containers and red bags
-Routine scheduled pickups

Price $35.95
Updates

Remember this is a half page flyer. Please remove pricing from all future work.

Target Market(s)

- Dentist
- Physicians
-Blood banks
-Tattoo parlors
-Laboratories
-Veterinarians

Industry/Entity Type

It Company

Colors
33b8a4

Requirements
Must have
• See my website www.korvanewaste.example

```html
<!DOCTYPE html>
<html lang="en">
<head>
<meta charset="utf-8">
<title>Korvane Waste – Half Page Mailer</title>
<link href="https://fonts.googleapis.com/css2?family=Oswald:wght@500&family=Questrial&family=Open+Sans:ital,wght@0,400;1,600&display=swap" rel="stylesheet">
<style>
  :root {
    --teal: #1fb3a0;
    --teal-soft: rgba(31, 179, 160, 0.82);
    --sky: #3aa9dc;
    --brand-green: #2b8a5a;
    --ink: #222;
    --paper: #fff;
    --backdrop: #2b2b2b;
    --rule: #9a9a9a;
  }
  * { box-sizing: border-box; margin: 0; padding: 0; }
  html, body { width: 1200px; height: 800px; overflow: hidden; }
  body { background: var(--backdrop); position: relative; font-family: "Questrial", sans-serif; }

  .card { position: absolute; width: 420px; height: 596px; background: var(--paper); overflow: hidden; }
  .card--front { left: 122px; top: 102px; }
  .card--back { left: 648px; top: 102px; }

  .brand { position: absolute; display: flex; align-items: center; gap: 8px; }
  .brand__dot { width: 30px; height: 30px; border-radius: 50%; background: var(--brand-green); }
  .brand__name { font-family: "Questrial", sans-serif; color: var(--brand-green); font-size: 21px; letter-spacing: 0.5px; white-space: nowrap; }
  .card--front .brand { left: 26px; top: 24px; }
  .card--back .brand { right: 20px; top: 32px; }
  .card--back .brand__dot { width: 22px; height: 22px; }
  .card--back .brand__name { font-size: 15px; }

  .front-header__contact { position: absolute; right: 18px; top: 14px; text-align: right; font-family: "Open Sans", sans-serif; }
  .front-header__line { font-size: 11px; line-height: 15px; color: var(--ink); display: flex; align-items: center; justify-content: flex-end; gap: 4px; }
  .front-header__tagline { margin-top: 4px; font-size: 12px; font-style: italic; font-weight: 600; color: var(--ink); }

  .photo { position: absolute; }
  .photo--surgery { left: 0; top: 74px; width: 420px; height: 224px;
    background: linear-gradient(160deg, #7f8f86 0%, #5d7fa8 45%, #3f6ea8 70%, #8da7c4 100%); }
  .photo--lab { left: 140px; top: 298px; width: 280px; height: 298px;
    background: linear-gradient(90deg, rgba(255,255,255,1) 0%, rgba(232,238,244,0.7) 30%, #c9d6e2 60%, #b8c4cf 100%); }
  .photo--doctor { left: 254px; top: 58px; width: 166px; height: 240px;
    background: linear-gradient(90deg, #fff 0%, #eef1f3 35%, #e4e8eb 100%); }

  .headline-panel { position: absolute; left: 0; top: 152px; width: 189px; height: 128px;
    background: var(--teal-soft); padding: 8px 0 0 20px; }
  .headline { font-family: "Oswald", sans-serif; font-weight: 500; font-size: 21px; line-height: 29px; color: #fff; text-transform: uppercase; }

  .section-tab { position: absolute; left: 0; height: 31px; background: var(--teal); color: #fff;
    font-family: "Questrial", sans-serif; font-weight: 400; font-size: 23px; line-height: 31px; padding-left: 26px;
    border-radius: 0 6px 6px 0; box-shadow: 2px 2px 3px rgba(0,0,0,0.2); }
  .card--front .section-tab { top: 326px; width: 229px; }
  .card--back .section-tab { top: 26px; width: 230px; font-size: 21px; padding-left: 28px; }

  .list { position: absolute; list-style: none; color: var(--ink); }
  .list li { display: flex; align-items: center; gap: 12px; white-space: nowrap; }
  .list li::before { content: ""; width: 10px; height: 10px; border: 1.5px solid var(--teal); border-radius: 50%; flex: none; }
  .list--serve { left: 30px; top: 372px; font-size: 19px; }
  .list--serve li { height: 29px; }
  .list--offer { left: 28px; top: 84px; font-size: 17.5px; }
  .list--offer li { height: 26px; gap: 9px; }

  .back-email { position: absolute; left: 28px; top: 240px; font-size: 15px; color: var(--teal); display: flex; align-items: center; gap: 8px; white-space: nowrap; }

  .info-bar { position: absolute; left: 0; width: 216px; background: var(--sky); color: #fff;
    font-size: 13.5px; line-height: 17px; padding-left: 27px; box-shadow: 2px 2px 3px rgba(0,0,0,0.2); }
  .info-bar--intro { top: 312px; height: 61px; padding-top: 8px; }
  .info-bar--web { top: 541px; height: 45px; padding-top: 6px; }

  .about { position: absolute; left: 28px; top: 386px; width: 172px; font-size: 11px; line-height: 15px;
    color: var(--teal); text-align: justify; }

  .stamp { position: absolute; left: 334px; top: 320px; width: 64px; height: 68px; border: 1px solid #666; }
  .address-line { position: absolute; left: 246px; width: 152px; border-top: 1px solid var(--rule); }
  .address-line--1 { top: 486px; }
  .address-line--2 { top: 506px; }
  .address-line--3 { top: 524px; }
</style>
</head>
<body>

<section class="card card--front">
  <div class="brand"><span class="brand__dot"></span><span class="brand__name">Korvane Waste</span></div>
  <div class="front-header__contact">
    <p class="front-header__line">
      <svg width="10" height="10" viewBox="0 0 10 10" aria-hidden="true"><circle cx="5" cy="5" r="4.2" fill="none" stroke="#1fb3a0" stroke-width="1.2"/><path d="M1 5h8M5 1c-2 2.5-2 5.5 0 8M5 1c2 2.5 2 5.5 0 8" fill="none" stroke="#1fb3a0" stroke-width="0.9"/></svg>
      www.korvanewaste.example
    </p>
    <p class="front-header__line">
      <svg width="11" height="8" viewBox="0 0 11 8" aria-hidden="true"><rect x="0.6" y="0.6" width="9.8" height="6.8" fill="none" stroke="#1fb3a0" stroke-width="1.1"/><path d="M0.8 0.8l4.7 3.8 4.7-3.8" fill="none" stroke="#1fb3a0" stroke-width="1"/></svg>
      info@korvanewsate.example
    </p>
    <p class="front-header__tagline">Compliant Waste Solutions</p>
  </div>

  <div class="photo photo--surgery" role="img" aria-label="Surgical team in blue scrubs and caps operating in a theatre"></div>
  <div class="headline-panel">
    <h1 class="headline">Now you have<br>options for your<br>medical waste<br>disposal</h1>
  </div>

  <div class="photo photo--lab" role="img" aria-label="Lab technicians in white coats examining a sample tube"></div>
  <h2 class="section-tab">WHO WE SERVE</h2>
  <ul class="list list--serve">
    <li>Dentist</li>
    <li>Physicians</li>
    <li>Blood banks</li>
    <li>Tattoo parlors</li>
    <li>Assisted living facilities</li>
    <li>Laboratories</li>
    <li>Veterinarians</li>
  </ul>
</section>

<section class="card card--back">
  <h2 class="section-tab">WHAT WE OFFER</h2>
  <div class="brand"><span class="brand__dot"></span><span class="brand__name">Korvane Waste</span></div>
  <div class="photo photo--doctor" role="img" aria-label="Smiling doctor in a white coat with a stethoscope"></div>
  <ul class="list list--offer">
    <li>Straight forward pricing</li>
    <li>No hidden fees</li>
    <li>No long term contracts</li>
    <li>Free containers and red bags</li>
    <li>Routine scheduled pickups</li>
  </ul>
  <p class="back-email">
    <svg width="14" height="10" viewBox="0 0 14 10" aria-hidden="true"><rect x="0.7" y="0.7" width="12.6" height="8.6" fill="none" stroke="#1fb3a0" stroke-width="1.3"/><path d="M0.9 0.9l6.1 4.8 6.1-4.8" fill="none" stroke="#1fb3a0" stroke-width="1.2"/></svg>
    info@korvanewsate.example
  </p>

  <p class="info-bar info-bar--intro">Korvane Waste provides regulated medical waste management solutions.</p>
  <p class="about">From collection to disposal, Korvane Waste is a provider of cost effective medical waste disposal in Kentuckiana and Southern Indiana. Maintain compliance with qualified collection, transport, and disposal of sharps and bio hazardous waste.</p>
  <p class="info-bar info-bar--web">To Know More Log in to<br>www.korvanewaste.example</p>

  <div class="stamp"></div>
  <div class="address-line address-line--1"></div>
  <div class="address-line address-line--2"></div>
  <div class="address-line address-line--3"></div>
</section>

</body>
</html>
```